Loomberry AI - Help users create their own recipe for a delicious AI treat!

Our company is an AI startup called Loomberrys. A Loomberry is an easy way to play with data (user can ask questions and get visualized answers about the dataset, sort of like QuillMate). Our users can "bake" their own Loomberrys by combining different sources of data.

We need a page that offers two things (both are required):

(1) TRY A LOOMBERRY --> Present a gallery of pre-made Loomberrys, each of which a user can click on and start playing with inside a popup iFrame. (visually, a Loomberry should be represented by some variation of our logo, attached). Designer does not need to worry about the iFrame popup.

(2) BAKE YOUR OWN LOOMBERRY --> Guide the user through making their own Loomberry recipe. The steps in making a Loomberry are:

A. Pick first ingredient - a Connector that imports the user's own data (visually, we present these options as logos for the Connector source, like Zentor, Pallomix, Brivane KLX, etc.).

B. Pick additional ingredients - the user can choose from 3rd-party cakes to combine with their own data added in (A). (visually, these 3rd-party cake options are presented as "mini" cakes, similar to our logo)

C. Once the ingredients are selected, the user can hit a BAKE button, and an iFrame popup opens, where user can play with the result. Designer does not need to worry about the iFrame popup.

We already have a web page and color scheme that we'd like this page to match (https://www.loomberrys.ai). The designer has freedom to play with format and try variations on the color scheme. The overall design should feel futuristic, fun, but also professional (like our logo).

Target Market(s)

Business users who want an easier way to get answers from large messy data

Industry/Entity Type

Tech/AI

Number of Pages Required

1 page

Font styles to use
Other font styles liked:
• Rubik

Requirements
Must have
• Full page design that matches current website (www.loomberrys.ai) and meets all requirements in the Project Description
Nice to have
• Included in the Project Description
Should not have
• Do not submit any designs that are too cartoonish or would not appeal to a business user

```html
<!DOCTYPE html>
<html lang="en">
<head>
<meta charset="utf-8">
<title>Loomberrys – Try &amp; Bake</title>
<link href="https://fonts.googleapis.com/css2?family=Rubik:wght@300;400;500;700&display=swap" rel="stylesheet">
<style>
:root{
  --bg-deep:#0f1730;
  --bg-mid:#1a2a52;
  --card:#1c2b4f;
  --card-line:#2c4469;
  --cyan:#25d0f0;
  --pink:#d77bb5;
  --text:#e9eef8;
  --muted:#aab4c8;
  --delete:#f06a8a;
}
*{box-sizing:border-box;margin:0;padding:0}
html,body{width:851px;height:1200px;overflow:hidden;background:var(--bg-deep)}
body{font-family:'Rubik',sans-serif;color:var(--text)}
.page{
  position:absolute;left:0;top:0;width:1440px;height:2031px;
  transform:scale(0.591);transform-origin:0 0;
  background:radial-gradient(ellipse 60% 45% at 50% 40%,var(--bg-mid),var(--bg-deep) 100%);
}
.abs{position:absolute}
.brand{left:100px;top:42px;display:flex;align-items:center;gap:10px;font-size:32px;font-weight:300;color:var(--text)}
.brand-dot{width:30px;height:30px;border-radius:50%;background:var(--cyan)}
.nav{top:54px;left:782px;display:flex;gap:26px;font-size:19px;font-weight:300}
.nav a{color:var(--text);text-decoration:none}
.demo-btn{left:1180px;top:40px;width:167px;height:52px;border-radius:26px;
  background:linear-gradient(90deg,var(--pink),var(--cyan));color:#0f1730;font-weight:500;font-size:17px;
  display:flex;align-items:center;justify-content:center}
.rule{left:0;width:202px;height:2px;background:linear-gradient(90deg,var(--pink),var(--cyan))}
.rule::after{content:"";position:absolute;right:-3px;top:-4px;width:10px;height:10px;border-radius:50%;background:var(--cyan)}
.sec-title{left:240px;font-size:28px;font-weight:700}
.sec-sub{left:240px;font-size:17px;font-weight:300}
.intro{left:687px;top:232px;width:530px;font-size:17px;line-height:29px;font-weight:300}
.card{width:280px;height:193px;background:var(--card);border:1px solid var(--card-line);border-radius:4px}
.card.is-selected{border:2px solid var(--cyan)}
.card .ver{position:absolute;left:12px;top:11px;font-size:13px;color:var(--muted)}
.card .size{position:absolute;right:10px;top:11px;font-size:13px;color:var(--muted)}
.card .mark{position:absolute;left:50%;top:34px;width:62px;height:62px;margin-left:-31px;border:3px solid #8a93a8;border-radius:6px;opacity:.8}
.card.is-selected .mark{border-color:var(--cyan);opacity:1}
.card .foot{position:absolute;left:0;right:0;top:133px;bottom:0;border-top:1px solid var(--card-line);padding:22px 12px 0;font-size:14px}
.note{font-size:13px;color:var(--cyan);text-align:center;width:280px}
.arrow{width:30px;height:54px}
.bake{left:641px;width:160px;height:52px;border-radius:26px;border:2px solid transparent;
  background:linear-gradient(var(--bg-deep),var(--bg-deep)) padding-box,linear-gradient(90deg,var(--pink),var(--cyan)) border-box;
  font-size:18px;font-weight:700;letter-spacing:2px;display:flex;align-items:center;justify-content:center}
.step{left:0;width:1440px;text-align:center}
.step-head{font-size:18px;font-weight:500;color:var(--cyan);display:flex;justify-content:center;align-items:center;gap:10px}
.step-num{width:26px;height:26px;border-radius:50%;border:2px solid var(--cyan);font-size:15px;display:flex;align-items:center;justify-content:center}
.step-text{font-size:13px;margin-top:12px}
.connector{width:280px;height:104px;border:2px solid var(--card-line);border-radius:3px;display:flex;align-items:center;justify-content:center;gap:14px}
.connector.is-configured{border-color:var(--cyan)}
.connector .dot{width:44px;height:44px;border-radius:50%}
.connector .name{font-size:28px;font-weight:500;line-height:1}
.connector .kind{font-size:22px;font-weight:300;color:var(--muted);line-height:1.1}
.divider{left:243px;top:1476px;width:953px;height:1px;background:var(--card-line)}
.mini{width:284px;height:156px;background:var(--card);border:2px solid var(--card-line);border-radius:6px}
.mini.is-done{border-color:var(--cyan)}
.mini .ver,.mini .size{position:absolute;top:10px;font-size:13px;color:var(--muted)}
.mini .ver{left:10px}.mini .size{right:12px}
.mini .mark{position:absolute;left:50%;top:30px;width:40px;height:40px;margin-left:-20px;border:3px solid #b6bdcc;border-radius:5px}
.mini.is-done .mark{border-color:var(--cyan)}
.mini .foot{position:absolute;left:0;right:0;top:94px;bottom:0;border-top:1px solid var(--card-line);display:flex;justify-content:space-between;align-items:center;padding:0 14px 0 10px;font-size:14px;letter-spacing:1px}
.cyan{color:var(--cyan)}
.slot{width:284px;height:156px;border:1px dashed var(--card-line);border-radius:6px}
.slot .mark{position:absolute;left:50%;top:26px;width:40px;height:40px;margin-left:-20px;border:3px solid #4c5875;border-radius:5px}
.add-btn{position:absolute;left:20px;top:90px;width:241px;height:40px;border-radius:20px;border:1px solid transparent;
  background:linear-gradient(var(--bg-deep),var(--bg-deep)) padding-box,linear-gradient(90deg,var(--pink),var(--cyan)) border-box;
  font-size:14px;letter-spacing:1px;display:flex;align-items:center;justify-content:center;gap:10px}
.plus{width:20px;height:20px;border-radius:50%;border:1px solid var(--text);display:flex;align-items:center;justify-content:center;font-size:15px;line-height:1}
.delete{left:243px;top:1779px;width:284px;text-align:center;font-size:13px;color:var(--delete)}
</style>
</head>
<body>
<main class="page">
  <header>
    <div class="abs brand"><span class="brand-dot"></span>loomberrys</div>
    <nav class="abs nav"><a href="#">Try Pippo</a><a href="#">About Us</a><a href="#">Contact Us</a></nav>
    <a class="abs demo-btn">Try Web Demo</a>
  </header>

  <section>
    <div class="abs rule" style="top:258px"></div>
    <h2 class="abs sec-title" style="top:232px">TRY A LOOMBERRY</h2>
    <p class="abs sec-sub" style="top:265px">Select&nbsp; a Pre-made Loomberry</p>
    <p class="abs intro">Lorem ipsum dolor sit amet, consectetur adipiscing elit, sed do eiusmod tempor incididunt ut labore et dolore magna aliqua.</p>

    <svg class="abs arrow" style="left:143px;top:584px" viewBox="0 0 30 54"><path d="M28 2 L3 27 L28 52" fill="none" stroke="#8a93a8" stroke-width="2"/></svg>
    <svg class="abs arrow" style="left:1268px;top:584px" viewBox="0 0 30 54"><path d="M2 2 L27 27 L2 52" fill="none" stroke="#8a93a8" stroke-width="2"/></svg>

    <div class="abs card is-selected" style="left:236px;top:396px"><span class="ver">V3.10.23</span><span class="size">5.3Gb</span><span class="mark"></span><div class="foot">SMB Accounting</div></div>
    <div class="abs note" style="left:236px;top:602px">Selected</div>
    <div class="abs card" style="left:580px;top:396px"><span class="ver">V1.03.24</span><span class="size">4.2Gb</span><span class="mark"></span><div class="foot">TORI Loomberry</div></div>
    <div class="abs card" style="left:924px;top:396px"><span class="ver">V1.01.22</span><span class="size">1.9Gb</span><span class="mark"></span><div class="foot">GORI Basic Loomberry</div></div>
    <div class="abs card" style="left:236px;top:632px"><span class="ver">V1.03.24</span><span class="size">4.2Gb</span><span class="mark"></span><div class="foot">TORI Loomberry</div></div>
    <div class="abs card" style="left:580px;top:632px"><span class="ver">V1.01.22</span><span class="size">1.9Gb</span><span class="mark"></span><div class="foot">GORI Basic Loomberry</div></div>
    <div class="abs card" style="left:924px;top:632px"><span class="ver">V1.03.24</span><span class="size">4.2Gb</span><span class="mark"></span><div class="foot">TORI Loomberry</div></div>

    <a class="abs bake" style="top:919px">BAKE</a>
  </section>

  <section>
    <div class="abs rule" style="top:1120px"></div>
    <h2 class="abs sec-title" style="top:1094px">Bake Your Own Loomberry</h2>
    <p class="abs sec-sub" style="top:1127px">Pick Your Own Ingredients</p>

    <div class="abs step" style="top:1211px">
      <div class="step-head"><span class="step-num">1</span>Pick Your First Ingredient</div>
      <p class="step-text">Select One Of The Following Dataset Providers To Start Working On</p>
    </div>

    <div class="abs connector" style="left:245px;top:1304px"><span class="dot" style="background:#1877f2"></span><div><div class="name">Pallomix</div><div class="kind">Dataset</div></div></div>
    <div class="abs connector" style="left:581px;top:1304px"><span class="dot" style="background:#f7a21b"></span><div class="name">Brivane KLX</div></div>
    <div class="abs connector is-configured" style="left:917px;top:1304px"><span class="dot" style="background:#4a86e8"></span><div><div class="name" style="font-weight:400">Zentor</div><div class="kind" style="color:var(--text)">Stackwell</div></div></div>
    <div class="abs note" style="left:917px;top:1420px">Configured</div>

    <div class="abs divider"></div>

    <div class="abs step" style="top:1522px">
      <div class="step-head"><span class="step-num">2</span>Additional Ingredient</div>
      <p class="step-text">Configure Your Own 3th Party Datasets, Once Configured You Can BAKE Your Loomberry</p>
    </div>

    <div class="abs mini is-done" style="left:243px;top:1613px"><span class="ver">V1.03.24</span><span class="size">1.5Gb</span><span class="mark"></span><div class="foot"><span>Cake LF87TTL</span><span class="cyan">100% Done</span></div></div>
    <div class="abs delete">Delete ⊗</div>
    <div class="abs mini" style="left:578px;top:1613px"><span class="ver">V1.0</span><span class="size">3.5Gb</span><span class="mark"></span><div class="foot cyan"><span>Loading...</span><span>35%</span></div></div>
    <div class="abs slot" style="left:913px;top:1613px"><span class="mark"></span><a class="add-btn">Add 3th Party Dataset <span class="plus">+</span></a></div>

    <a class="abs bake" style="top:1861px">BAKE</a>
  </section>
</main>
</body>
</html>
```